Student Card

we are college and require a student card which we issue on enlroment to students, just like a univeristy.

Baisic information need to be placed is:
Student photo
student ID
date of birth
exp date

our college contact details on the rear
its a tool for branding so its important the theme is in line with our colours and logo, please view our website www.hartwellcollege.net.au

Industry/Entity Type

College

```html
<!DOCTYPE html>
<html lang="en">
<head>
<meta charset="utf-8">
<title>Hartwell College Student Card</title>
<link rel="stylesheet" href="https://fonts.googleapis.com/css2?family=Archivo+Black&family=Archivo+Narrow:wght@700&display=swap">
<style>
  :root {
    --ink: #0c0c0c;
    --band-top: #2fd3dc;
    --band-top-deep: #22c2cf;
    --band-bottom: #3cf3fa;
    --band-bottom-deep: #2ee3ee;
    --divider: #a9fbff;
    --brand-blue: #1b46e6;
    --photo-light: #f4f4f4;
    --photo-mid: #d9d9d9;
    --frame: #111;
  }
  html, body {
    margin: 0;
    padding: 0;
    width: 1200px;
    height: 643px;
    overflow: hidden;
    background: #ffffff;
  }
  .card {
    position: relative;
    width: 1200px;
    height: 643px;
    box-sizing: border-box;
    border: 4px solid var(--frame);
    background: linear-gradient(180deg, var(--band-bottom) 0%, var(--band-bottom-deep) 100%);
    overflow: hidden;
    font-family: "Archivo Black", "Arial Black", sans-serif;
    color: var(--ink);
  }
  .card-header {
    position: absolute;
    left: 0;
    top: 0;
    width: 100%;
    height: 308px;
    background: linear-gradient(180deg, var(--band-top) 0%, var(--band-top-deep) 100%);
    border-bottom: 4px solid var(--divider);
  }
  .brand {
    position: absolute;
    left: 30px;
    top: 20px;
    width: 410px;
    height: 280px;
    display: flex;
    flex-direction: column;
    align-items: center;
    justify-content: center;
    gap: 26px;
  }
  .brand-mark {
    width: 120px;
    height: 120px;
    background: var(--brand-blue);
  }
  .brand-name {
    font-size: 34px;
    letter-spacing: 1px;
    color: var(--brand-blue);
    white-space: nowrap;
  }
  .card-title {
    position: absolute;
    left: 440px;
    right: 0;
    top: 62px;
    margin: 0;
    text-align: center;
    font-weight: 400;
    line-height: 1;
    text-shadow: 0 0 3px #fff, 0 0 3px #fff, 0 0 2px #fff;
  }
  .card-title .title-lead {
    display: block;
    font-size: 100px;
    letter-spacing: 1px;
  }
  .card-title .title-college {
    display: block;
    font-size: 78px;
    margin-top: 20px;
    letter-spacing: 1px;
  }
  .student-photo {
    position: absolute;
    left: 26px;
    top: 324px;
    width: 360px;
    height: 300px;
    border-radius: 6px;
    background: radial-gradient(ellipse at center, var(--photo-light) 0%, var(--photo-light) 70%, var(--photo-mid) 100%);
    box-shadow: inset 0 0 14px rgba(255,255,255,0.9), 0 0 6px rgba(255,255,255,0.8);
  }
  .student-fields {
    position: absolute;
    left: 410px;
    right: 14px;
    top: 350px;
    margin: 0;
    padding: 0;
    list-style: none;
  }
  .field {
    display: flex;
    align-items: baseline;
    white-space: nowrap;
  }
  .field-label {
    margin-right: 22px;
  }
  .field-line {
    flex: 1;
    border-bottom: 6px dotted var(--ink);
    transform: translateY(-4px);
  }
  .field-id {
    font-size: 40px;
    letter-spacing: 1.5px;
  }
  .field-dob {
    margin-top: 38px;
    margin-right: 72px;
    font-family: "Archivo Narrow", "Arial Narrow", sans-serif;
    font-weight: 700;
    font-size: 42px;
  }
  .field-exp {
    margin-top: 36px;
    font-size: 34px;
    letter-spacing: 1.5px;
  }
</style>
</head>
<body>
  <main class="card">
    <header class="card-header">
      <div class="brand">
        <div class="brand-mark"></div>
        <div class="brand-name">HARTWELL COLLEGE</div>
      </div>
      <h1 class="card-title">
        <span class="title-lead">Student of</span>
        <span class="title-college">Hartwell College</span>
      </h1>
    </header>

    <div class="student-photo" role="img" aria-label="Student photo"></div>

    <ul class="student-fields">
      <li class="field field-id"><span class="field-label">Student ID:</span><span class="field-line"></span></li>
      <li class="field field-dob"><span class="field-label">Date of Birth:</span><span class="field-line"></span></li>
      <li class="field field-exp"><span class="field-label">Exp Date:</span><span class="field-line"></span></li>
    </ul>
  </main>
</body>
</html>
```